Energy Healing for pregnant women postcard

I am an intuitive energy healer specializing in the care of pregnant women and their babies. I have an existing logo that is attached that should be placed on the card,sizing is at your discretion, recolor as needed. The message of the card should be one that conveys tranquility, growth, life and light. Images of pregnancy and motherhood could also fit well on the card, but that is not required if the preceding messages can be conveyed through other imagery. Also on the card, the following should appear: (company name and tag line)Positivity & JoyHealing the mind, body, spirit and soul with Energy provided to all living things by the Universe. Space should be left for my name and credentials on the front, while the address space on the back will be used for more contact information. Opposite the address block on the back, please leave room for a text box that will include benefits of the services. About 2"x3" should suffice.

Target Market(s)

Pregnant women and newly post-partum women

Industry/Entity Type

Health And Wellness

Font styles to use
Script

Colors
b05ba4
b768aa
d3a5cc
ecdaeb
e7f5f8
cfdeed
cee9f5
85cae6

Requirements
Must have
• Company logo. Company name. Tag line. Individual name and certifications
Nice to have
• Pictures or images that convey peace, tranquility healing and growth.
Should not have
• Anything harsh.

```html
<!DOCTYPE html>
<html lang="en">
<head>
<meta charset="utf-8">
<title>Harbor &amp; Fern – Postcard</title>
<link href="https://fonts.googleapis.com/css2?family=Dancing+Script:wght@600&family=Nobile&display=swap" rel="stylesheet">
<style>
  :root {
    --bg: #efedea;
    --plum: #b05ba4;
    --plum-soft: #b768aa;
    --lilac: #d3a5cc;
    --blush: #ecdaeb;
    --panel: rgba(250, 249, 246, 0.93);
    --ink: #3d3a38;
    --white: #ffffff;
    --line: #8a8a8a;
    --gold-1: #f6ead0;
    --gold-2: #e3c48e;
    --gold-3: #c99558;
    --sky-1: #cee9f5;
    --sky-2: #85cae6;
  }
  * { box-sizing: border-box; margin: 0; padding: 0; }
  html, body { width: 1200px; height: 1000px; overflow: hidden; }
  body { background: var(--bg); position: relative; font-family: "Nobile", sans-serif; }

  .card { position: absolute; box-shadow: 0 6px 18px rgba(0,0,0,0.18); overflow: hidden; }

  /* Front */
  .card-front { left: 50px; top: 30px; width: 680px; height: 500px; }
  .front-photo {
    position: absolute; inset: 0;
    background: radial-gradient(ellipse at 70% 20%, var(--gold-1) 0%, var(--gold-2) 45%, var(--gold-3) 100%);
  }
  .brand-mark { position: absolute; left: 24px; top: 40px; display: flex; align-items: center; gap: 8px; }
  .brand-mark .dot { width: 14px; height: 14px; border-radius: 50%; background: var(--plum); }
  .brand-mark .brand-name { font-family: "Nobile", sans-serif; font-size: 15px; color: var(--plum); }
  .front-panel {
    position: absolute; left: 390px; top: 22px; width: 250px; height: 478px;
    background: var(--panel); text-align: center; padding-top: 34px;
  }
  .front-title { font-family: "Dancing Script", cursive; color: var(--plum); font-size: 42px; line-height: 1.1; }
  .benefits { list-style: none; margin-top: 30px; font-size: 15.5px; line-height: 1.5; color: var(--ink); padding: 0 16px; }
  .front-signature { margin-top: 34px; font-family: "Dancing Script", cursive; color: var(--plum); font-size: 24px; line-height: 1.15; }

  /* Back */
  .card-back { left: 590px; top: 520px; width: 560px; height: 440px; background: var(--white); }
  .back-panel { position: absolute; left: 0; top: 0; width: 305px; height: 375px; background: var(--plum); text-align: center; padding-top: 22px; color: var(--white); }
  .back-name { font-family: "Dancing Script", cursive; font-size: 29px; line-height: 1.2; }
  .credentials { list-style: none; margin-top: 14px; font-family: "Dancing Script", cursive; font-size: 17px; line-height: 1.35; }
  .credentials li::before { content: "\2713\00a0"; }
  .photo-grid { position: absolute; left: 22px; top: 178px; display: grid; grid-template-columns: 128px 128px; gap: 10px 14px; }
  .photo-grid > div { height: 80px; border: 3px solid var(--blush); }
  .photo-a { background: linear-gradient(180deg, #f1efe6, #9aa6a1); }
  .photo-b { background: linear-gradient(180deg, #fbfbf6, #6f9a70); }
  .photo-c { background: linear-gradient(180deg, var(--sky-1), var(--sky-2)); }
  .photo-d { background: linear-gradient(180deg, var(--sky-2) 0%, var(--sky-1) 55%, #e7d3b4 56%, #e2cca8 100%); }
  .stamp-box { position: absolute; right: 26px; top: 22px; width: 62px; height: 72px; border: 1.5px solid var(--line); }
  .address-lines { position: absolute; left: 372px; top: 180px; width: 148px; }
  .address-lines span { display: block; height: 1.5px; background: var(--line); margin-bottom: 28px; }
</style>
</head>
<body>
  <section class="card card-front">
    <div class="front-photo" role="img" aria-label="Photo of a woman with long hair, eyes closed, face turned up to warm golden sunlight"></div>
    <div class="brand-mark"><span class="dot"></span><span class="brand-name">Harbor &amp; Fern</span></div>
    <div class="front-panel">
      <h1 class="front-title">Harbor<br>&amp; Fern</h1>
      <ul class="benefits">
        <li>Deep relaxation</li>
        <li>Decrease anxiety</li>
        <li>Decrease stress</li>
        <li>Decrease discomforts</li>
        <li>Promote feelings of wellbeing</li>
        <li>Promote balance</li>
        <li>Relieve physical discomforts of pregnancy</li>
      </ul>
      <p class="front-signature">Maren L. Whitfield<br>MSN, RCMT</p>
    </div>
  </section>

  <section class="card card-back">
    <div class="back-panel">
      <h2 class="back-name">Maren L. Whitfield<br>MSN, RCMT</h2>
      <ul class="credentials">
        <li>Reiki Master Teacher</li>
        <li>Archangelic Light Master Teacher</li>
      </ul>
      <div class="photo-grid">
        <div class="photo-a" role="img" aria-label="Person meditating before a misty sunlit valley"></div>
        <div class="photo-b" role="img" aria-label="Man with arms outstretched in bright sunlight among trees"></div>
        <div class="photo-c" role="img" aria-label="Woman by the sea looking up at a blue sky"></div>
        <div class="photo-d" role="img" aria-label="Woman meditating on a sunny beach"></div>
      </div>
    </div>
    <div class="stamp-box"></div>
    <div class="address-lines"><span></span><span></span><span></span><span></span></div>
  </section>
</body>
</html>
```